Australian HR Consultancy Company Brochure (and more!). Our tagline "Start something amazing."

We are a start-up HR and Recruitment consultancy. We have a group of young, passionate and top performing staff who assist companies with driving their workforce productivity, keeping employees happy, hiring fantastic people and ensuring legal compliance across the HR field.

We work across a variety of sectors such as mining, Not for Profits, Finance, Accounting, Health etc so are not pigeon-holed to one particular group. We tend to deal with medium sized businesses.

Our team is professional and corporate but down to earth and approachable. We have unique offerings in terms of our services and our pricing. We deliver exceptional value to our clients and build long term mutually beneficial relationships. We care about giving back to the community and doing the right thing by everyone we deal with.

Our design should communicate that we are corporate and professional but not uptight 'suits', that we are fresh and engaging. Clear, concise, crisp but not cold.

Thinking 6 page brochure.

We have a variety of colours in our logo and tend to lean towards fresh shades of blue and green but are definitely open to other colours such as purple, pink, orange etc. We would prefer the brochure to be in landscape format (like a powerpoint presentation) as apparently that's easier to read? but open to your expert suggestions!

Target Market(s)

Medium sized business across all industries but within the professional area ie finance, mining, health.

Industry/Entity Type

It Company

Colors
33b8a4
33a6d7
0592cd
85cae6
86cfc6
b768aa

Requirements
Must have
• Needs to be editable version as we will be changing our tagline and about us in the new year.

```html
<!DOCTYPE html>
<html lang="en">
<head>
<meta charset="utf-8">
<title>TeamLaunch Brochure Spreads</title>
<link href="https://fonts.googleapis.com/css2?family=Roboto:wght@400;500;700;900&display=swap" rel="stylesheet">
<style>
  :root{
    --bg:#c4c3c0;
    --blue:#29a9df;
    --blue-deep:#1a8fcb;
    --blue-pale:#cfe9f6;
    --navy:#2b3a8c;
    --ink:#1f2a3a;
    --orange:#f08a24;
    --purple:#7b3fa0;
    --paper:#f3f4f5;
    --white:#ffffff;
  }
  *{box-sizing:border-box;margin:0;padding:0}
  html,body{width:858px;height:1200px;overflow:hidden}
  body{background:var(--bg);font-family:'Roboto',sans-serif;color:var(--ink);position:relative}
  .spread{position:absolute;left:49px;width:760px;height:340px;display:flex;box-shadow:0 8px 22px rgba(0,0,0,.22)}
  .spread--cover{top:40px}
  .spread--about{top:430px}
  .spread--services{top:820px}
  .page{position:relative;width:380px;height:340px;overflow:hidden;background:var(--paper)}
  .page svg.bg{position:absolute;inset:0;width:100%;height:100%}
  .abs{position:absolute}
  .photo-note{display:block}

  /* cover */
  .brand{display:flex;align-items:center;gap:7px;font-weight:700;color:var(--navy);font-size:20px}
  .brand__dot{width:11px;height:11px;border-radius:50%;background:var(--purple)}
  .back-contact{left:170px;top:140px;color:var(--white);font-size:9.5px;line-height:1.5}
  .back-contact .brand{margin-bottom:10px}
  .back-contact .team{margin-top:14px}
  .front-brand{left:36px;top:38px}
  .front-brand .brand{font-size:16px}
  .tagline{left:150px;top:225px;color:var(--white);font-weight:700;font-size:26px;line-height:1.05}

  /* about */
  .about-label{left:14px;top:210px;transform:rotate(-90deg);transform-origin:left top;color:var(--orange);font-size:16px;font-weight:500}
  .about-box{left:58px;top:60px;width:270px;height:232px;background:var(--blue);padding:16px 16px;color:var(--white);font-size:12.5px;line-height:1.32}
  .list{list-style:none;font-size:8.5px;line-height:1.45}
  .list li::before{content:"- ";}
  .hr-intro{left:22px;top:40px;width:170px;font-size:8.5px;font-weight:500;line-height:1.3}
  .hr-list{left:30px;top:72px;width:165px}
  .hr-title{left:22px;top:262px;font-size:19px;font-weight:700;color:var(--ink)}
  .url{right:16px;bottom:12px;color:var(--white);font-size:9px}

  /* services */
  .strat-title{left:14px;top:38px;color:var(--white);font-size:17px;font-weight:500}
  .strat-intro{left:178px;top:18px;width:190px;font-size:8.5px;line-height:1.3;font-weight:500}
  .strat-list{left:185px;top:44px}
  .staff-title{left:130px;top:160px;font-size:16px;font-weight:700}
  .staff-sub{left:130px;top:180px;font-size:8.5px;line-height:1.35}
  .staff-list-a{left:20px;top:266px;color:var(--white)}
  .staff-list-b{left:214px;top:210px;color:var(--white)}
  .ws-kicker{left:26px;top:22px;color:var(--white);font-size:8.5px;line-height:1.25}
  .ws-title{left:24px;top:46px;color:var(--white);font-size:30px;font-weight:900;letter-spacing:.5px}
  .ws-intro{left:22px;top:150px;width:150px;font-size:8.5px;font-weight:500;line-height:1.3}
  .ws-list{left:28px;top:182px}
  .ws-note{left:12px;bottom:12px;color:var(--white);font-size:8px;font-weight:500}
</style>
</head>
<body>

<!-- Spread 1: back and front cover -->
<section class="spread spread--cover">
  <div class="page page--back">
    <svg class="bg" viewBox="0 0 380 340" aria-hidden="true">
      <rect width="380" height="340" fill="var(--blue)"/>
      <path d="M250 0 H380 V40 Q320 20 250 0Z" fill="var(--blue-pale)"/>
    </svg>
    <svg class="bg" viewBox="0 0 380 340" role="img" aria-label="Photo of a training session with attendees facing a presentation screen">
      <defs><linearGradient id="g1" x1="0" y1="0" x2="1" y2="1"><stop offset="0" stop-color="#d9dde2"/><stop offset="1" stop-color="#8c8a8a"/></linearGradient></defs>
      <polygon points="0,0 210,0 150,340 0,340" fill="url(#g1)"/>
    </svg>
    <div class="abs back-contact">
      <div class="brand"><span class="brand__dot"></span>TeamLaunch</div>
      <p>Start a conversation with us</p>
      <p>www.teamlaunch.com.au</p>
      <p>Ph: 1300 000 000</p>
      <p class="team">Our Leadership Team – Ben, Tara, Mia.</p>
    </div>
  </div>
  <div class="page page--front">
    <svg class="bg" viewBox="0 0 380 340" aria-hidden="true">
      <defs><linearGradient id="g2" x1="0" y1="0" x2="0" y2="1"><stop offset="0" stop-color="var(--blue-pale)"/><stop offset="1" stop-color="#f6fafc"/></linearGradient></defs>
      <rect width="380" height="340" fill="url(#g2)"/>
      <path d="M0 140 Q150 110 300 200 L380 200 V340 H0Z" fill="var(--blue)"/>
      <path d="M0 120 Q150 95 300 180" stroke="var(--white)" stroke-width="6" fill="none" opacity=".8"/>
    </svg>
    <svg class="bg" viewBox="0 0 380 340" role="img" aria-label="Photo of a businessman in glasses working on a tablet">
      <defs><linearGradient id="g3" x1="0" y1="0" x2="1" y2="1"><stop offset="0" stop-color="#c8d4e2"/><stop offset="1" stop-color="#2d3f66"/></linearGradient></defs>
      <polygon points="190,0 380,0 380,230 310,200" fill="url(#g3)"/>
    </svg>
    <div class="abs front-brand"><div class="brand"><span class="brand__dot"></span>TeamLaunch</div></div>
    <h1 class="abs tagline">Start<br>something<br>amazing.</h1>
  </div>
</section>

<!-- Spread 2: about us and HR consulting -->
<section class="spread spread--about">
  <div class="page">
    <svg class="bg" viewBox="0 0 380 340" role="img" aria-label="Black and white photo of a busy office workspace">
      <defs><linearGradient id="g4" x1="0" y1="0" x2="1" y2="1"><stop offset="0" stop-color="#e6e6e6"/><stop offset="1" stop-color="#6e6e6e"/></linearGradient></defs>
      <rect width="380" height="340" fill="url(#g4)"/>
    </svg>
    <h2 class="abs about-label">About Us</h2>
    <div class="abs about-box">
      <p>TeamLaunch is an innovative industry leader in the provision of human resources, industrial relations and recruitment managed services. Our unique approach enables us to meet the challenges and demands of a diverse group of contemporary Australian businesses.</p>
      <p>We are committed to delivering exceptional service and value that ensures the best outcomes for our long-term business partnerships.</p>
    </div>
  </div>
  <div class="page">
    <svg class="bg" viewBox="0 0 380 340" aria-hidden="true">
      <rect width="380" height="340" fill="var(--paper)"/>
      <line x1="190" y1="26" x2="380" y2="22" stroke="var(--blue)" stroke-width="2"/>
      <path d="M0 300 Q200 250 380 200 V340 H0Z" fill="var(--blue)"/>
      <polygon points="22,28 30,20 30,34" fill="var(--purple)"/>
      <polygon points="44,22 52,30 40,32" fill="var(--blue)"/>
      <polygon points="60,40 68,34 68,46" fill="var(--orange)"/>
      <polygon points="258,6 268,6 263,14" fill="#f2c233"/>
      <polygon points="236,230 246,224 246,236" fill="var(--orange)"/>
    </svg>
    <svg class="bg" viewBox="0 0 380 340" role="img" aria-label="Photo of a presenter training a seated audience">
      <defs><linearGradient id="g5" x1="0" y1="0" x2="1" y2="1"><stop offset="0" stop-color="#e1e5e9"/><stop offset="1" stop-color="#9a7f6e"/></linearGradient></defs>
      <rect x="195" y="40" width="185" height="140" fill="url(#g5)"/>
    </svg>
    <p class="abs hr-intro">HR FOUNDATIONS - Building the HR foundations for legal compliance &amp; employee management</p>
    <ul class="abs list hr-list">
      <li>Employment Contracts &amp; Agreements</li>
      <li>Organisational Structure &amp; Design</li>
      <li>Terminations &amp; FairWork Advice</li>
      <li>Performance Management</li>
      <li>Recruitment &amp; Onboarding</li>
      <li>Remuneration &amp; Benefits</li>
      <li>HR Policies &amp; Procedures</li>
      <li>Workplace Investigations</li>
    </ul>
    <h2 class="abs hr-title">HR CONSULTING</h2>
    <p class="abs url">www.teamlaunch.com.au</p>
  </div>
</section>

<!-- Spread 3: strategic HR, staffing, workshops -->
<section class="spread spread--services">
  <div class="page">
    <svg class="bg" viewBox="0 0 380 340" aria-hidden="true">
      <rect width="380" height="340" fill="var(--paper)"/>
      <polygon points="0,30 170,20 170,130 0,170" fill="var(--navy)"/>
      <path d="M0 250 Q200 200 380 160 V340 H0Z" fill="var(--blue)"/>
      <polygon points="30,232 40,226 40,240" fill="var(--purple)"/>
    </svg>
    <svg class="bg" viewBox="0 0 380 340" role="img" aria-label="Photo of colleagues meeting around a desk">
      <defs><linearGradient id="g6" x1="0" y1="0" x2="1" y2="1"><stop offset="0" stop-color="#dcd4cc"/><stop offset="1" stop-color="#7d6f66"/></linearGradient></defs>
      <rect x="22" y="66" width="130" height="76" fill="url(#g6)"/>
    </svg>
    <h2 class="abs strat-title">STRATEGIC HR</h2>
    <p class="abs strat-intro">Driving organisational success through strategic people design.</p>
    <ul class="abs list strat-list">
      <li>Leadership Development</li>
      <li>Organisational Design</li>
      <li>Change Management</li>
      <li>Culture Programs</li>
      <li>Organisational Capabilities</li>
      <li>Executive &amp; Leadership Coaching</li>
      <li>Employee Engagement &amp; Retention</li>
      <li>Talent Attraction &amp; Acquisition</li>
    </ul>
    <h2 class="abs staff-title">PROFESSIONAL STAFFING</h2>
    <p class="abs staff-sub">Start hiring incredible people<br>Matching great organisations to great people</p>
    <ul class="abs list staff-list-b">
      <li>Recruitment Admin Support</li>
      <li>Manager Interview Training</li>
      <li>Talent Attraction &amp;<br>&nbsp;&nbsp;Acquisition Programs</li>
      <li>xxxx</li>
    </ul>
    <ul class="abs list staff-list-a">
      <li>Executive Search</li>
      <li>Recruitment Processing Outsourcing (RPO)</li>
      <li>Contingent &amp; Retained Services</li>
      <li>Permanent Recruitment</li>
    </ul>
  </div>
  <div class="page">
    <svg class="bg" viewBox="0 0 380 340" aria-hidden="true">
      <rect width="380" height="340" fill="var(--paper)"/>
      <polygon points="0,0 380,0 380,60 0,140" fill="var(--blue)"/>
      <polygon points="150,0 380,0 380,80 120,120" fill="var(--navy)"/>
      <path d="M0 320 Q200 270 380 230 V340 H0Z" fill="var(--blue)"/>
      <polygon points="345,14 355,14 350,22" fill="#f2c233"/>
      <polygon points="110,240 120,234 120,248" fill="var(--purple)"/>
      <polygon points="160,226 170,232 158,236" fill="var(--orange)"/>
      <polygon points="238,188 246,182 246,194" fill="var(--blue)"/>
    </svg>
    <svg class="bg" viewBox="0 0 380 340" role="img" aria-label="Overhead photo of a team workshop table with laptops and notes">
      <defs><linearGradient id="g7" x1="0" y1="0" x2="1" y2="1"><stop offset="0" stop-color="#c89a6a"/><stop offset="1" stop-color="#6e4e36"/></linearGradient></defs>
      <rect x="180" y="80" width="175" height="100" fill="url(#g7)"/>
    </svg>
    <p class="abs ws-kicker">Let's start<br>developing your team.</p>
    <h2 class="abs ws-title">WORKSHOPS</h2>
    <p class="abs ws-intro">Customised programs designed to make a strategic impact on your organisation and leadership.</p>
    <ul class="abs list ws-list">
      <li>Leadership Development</li>
      <li>Team Building</li>
      <li>Change Management</li>
      <li>Culture Building</li>
      <li>Management Basics</li>
    </ul>
    <p class="abs ws-note">Presented as 1-1.5 hour 'Lunch 'N' Learns', half day or full day workshops as requested across:</p>
  </div>
</section>

</body>
</html>
```